Business card / stationery design
Pemberton Hale Warrick
Project: Business card / stationery design
Business card / stationery design - Engineering
Creative Brief
Use specific fonts
Gill Sans MT, Calibri, Corbel, Lucida Sans UC or similar
Professional
Derek R. Pemberton, P.E., LEED A.P., CPMP
Principal
4738 E. Harrowgate Ave., Suite C-212B, Springfield, Missouri 65809
dpemberton@pembertonhalewarrick.example
www.pembertonhalewarrick.example
We would like to use only the logo from the attached file. We like the current color arrangement, but would be interested in seeing it in other colors. Also the slightly gray color behind the logo should just be white or whatever the background color is. A couple of examples are attached. The main text adjacent to the logo should read: Pemberton Hale Warrick. Secondary text will be similar to: Engineering & Energy Services.
We are interested in your ideas.

```html
<!DOCTYPE html>
<html lang="en">
<head>
<meta charset="utf-8">
<title>Pemberton Hale Warrick – Business Cards</title>
<link href="https://fonts.googleapis.com/css2?family=Cabin:wght@400;500;600&display=swap" rel="stylesheet">
<style>
  :root{
    --stage:#e4e2df;
    --ink:#2b2f33;
    --ink-soft:#5d6268;
    --blue:#1f79c2;
    --blue-deep:#0c4f8e;
    --green:#6fb83a;
    --green-light:#a4d24a;
    --white:#ffffff;
  }
  *{box-sizing:border-box;margin:0;padding:0}
  html,body{width:1200px;height:724px;overflow:hidden}
  body{background:var(--stage);font-family:"Cabin",sans-serif;color:var(--ink);position:relative}
  .card{position:absolute;width:442px;height:248px;border-radius:18px;overflow:hidden;box-shadow:0 3px 10px rgba(0,0,0,.25)}
  .card--contact{left:160px;top:92px;background:linear-gradient(180deg,#ffffff 0%,#f4f5f6 60%,#e4e6e8 100%)}
  .card--blue{left:632px;top:92px;background:radial-gradient(ellipse at 45% 40%,#2f92d6 0%,var(--blue-deep) 80%)}
  .card--white{left:160px;top:362px;background:linear-gradient(180deg,#ffffff 0%,#f3f4f5 70%,#e6e8ea 100%)}
  .card--green{left:632px;top:362px;background:radial-gradient(ellipse at 40% 40%,#c3e56a 0%,var(--green) 85%)}

  .brand{position:absolute;display:flex;flex-direction:column;align-items:center;text-align:center}
  .brand__square{width:48px;height:48px;background:var(--green);margin-bottom:14px}
  .brand__name{font-size:22px;font-weight:500;letter-spacing:.08em;text-transform:uppercase;white-space:nowrap}
  .brand__tagline{font-size:13px;margin-top:4px;letter-spacing:.02em;white-space:nowrap}
  .card--contact .brand{left:12px;top:58px;width:194px}
  .card--contact .brand__square{width:40px;height:40px;margin-bottom:10px}
  .card--contact .brand__name{font-size:12.5px;letter-spacing:.05em;color:var(--ink)}
  .card--contact .brand__tagline{font-size:10px;color:var(--ink-soft)}
  .card--centered .brand{left:0;right:0;top:66px}
  .card--blue .brand__name{color:#f2f6fa}
  .card--blue .brand__tagline{color:var(--green-light)}
  .card--blue .brand__square{background:var(--green-light)}
  .card--white .brand__name{color:var(--ink)}
  .card--white .brand__tagline{color:var(--blue)}
  .card--green .brand__name{color:#1c3350}
  .card--green .brand__tagline{color:#1c3350}
  .card--green .brand__square{background:var(--blue-deep)}

  .person{position:absolute;left:214px;top:34px;width:216px}
  .person__line{display:flex;align-items:baseline;gap:8px;white-space:nowrap}
  .person__name{font-size:14px;font-weight:600;color:var(--blue)}
  .person__role{font-size:10px;color:var(--ink-soft);border-left:1px solid #b5b9bd;padding-left:8px}
  .person__creds{font-size:9px;color:var(--ink-soft);margin-top:2px}
  .contact{list-style:none;margin-top:18px}
  .contact li{display:flex;align-items:flex-start;gap:8px;font-size:8px;line-height:1.3;color:var(--ink-soft);margin-bottom:6px;white-space:nowrap}
  .contact svg{flex:none;width:10px;height:10px;fill:var(--blue)}
</style>
</head>
<body>

<section class="card card--contact">
  <div class="brand">
    <div class="brand__square"></div>
    <div class="brand__name">Pemberton Hale Warrick</div>
    <div class="brand__tagline">Engineering &amp; Energy Services</div>
  </div>
  <div class="person">
    <div class="person__line">
      <span class="person__name">Derek R. Pemberton</span>
      <span class="person__role">Principal</span>
    </div>
    <div class="person__creds">P.E., LEED A.P., CPMP</div>
    <ul class="contact">
      <li><svg viewBox="0 0 10 10"><path d="M5 1 1 5h1.5v4h2.2V6.5h.6V9h2.2V5H9z"/></svg><span>4738 E. Harrowgate Ave.,<br>Suite C-212B, Larkmoor, Oregon 97431</span></li>
      <li><svg viewBox="0 0 10 10"><rect x="2.5" y="1" width="5" height="8" rx="1"/></svg><span>555-204-3318</span></li>
      <li><svg viewBox="0 0 10 10"><path d="M2 1h2l1 2.5-1.2 1a5 5 0 0 0 2.7 2.7l1-1.2L10 7v2c-4.5 0-8-3.5-8-8z"/></svg><span>555-204-3390</span></li>
      <li><svg viewBox="0 0 10 10"><path d="M1 2h8v6H1zm.8.8L5 5.3 8.2 2.8z"/></svg><span>dpemberton@pembertonhalewarrick.example</span></li>
      <li><svg viewBox="0 0 10 10"><circle cx="5" cy="5" r="4"/></svg><span>www.pembertonhalewarrick.example</span></li>
    </ul>
  </div>
</section>

<section class="card card--blue card--centered">
  <div class="brand">
    <div class="brand__square"></div>
    <div class="brand__name">Pemberton Hale Warrick</div>
    <div class="brand__tagline">Engineering &amp; Energy Services</div>
  </div>
</section>

<section class="card card--white card--centered">
  <div class="brand">
    <div class="brand__square"></div>
    <div class="brand__name">Pemberton Hale Warrick</div>
    <div class="brand__tagline">Engineering &amp; Energy Services</div>
  </div>
</section>

<section class="card card--green card--centered">
  <div class="brand">
    <div class="brand__square"></div>
    <div class="brand__name">Pemberton Hale Warrick</div>
    <div class="brand__tagline">Engineering &amp; Energy Services</div>
  </div>
</section>

</body>
</html>
```